Commercial Real Estate Company Needs an Awesome Flyer Design for their Oceanfront Property

We need a 2-page flyer or our Class A Oceanfront Property in Santa Monica, California. Approximately 16,149 square feet of Class A rare oceanfront office space with private balconies will be in available 4th Quarter of 2014. The SPACE has not been on the market for over 20 YEARS!

I attached our Previous 2-page flyer for the 2,353 square feet. We need a new vibrant, modern flyer that will attract Tech, Entertainment, Financial, and Marketing Companies to our building. Also, the 2nd Floor Space Plan is attached.

Also, please check out our website www.verlindeproperty.com. We would like to use the colors of our website and logo to incorporate with the flyer.

I updated the Must Have's on the Listing!

Target Market(s)

Entertainment, Financial, Tech Companies

Industry/Entity Type

Real Estate

Requirements
Must have
• Our Company Logo, Company, Leasing Agents On the First and 2nd Page

Trevor L. Ashdown (310) 555-0142
trev@verlindeproperty.com

Mark Oda (310) 555-0187
mark@verlindeproperty.com

Verlinde Property.
5127 N Harlow Ave, Suite 210
West Hollywood, Ca. 90069
(310) 555-0142
www.verlindeproperty.com

Also, the Front Page should indicate

"Rare Class A Oceanfront Office Space in the heart of Santa Monica"
"2nd Floor Office Space consisting of 16,159 square feet with private balconies."
Nice to have
• Please use description of the office building. You can omit whatever you think is unnecessary

"Bellhaven Court is one of Santa Monica's rare commercial properties that is both strategically located in the city's burgeoning central business district, yet ideally positioned on palm-lined Ocean Ave directly across from the Pacific Ocean. Built in 1987, the 3-story mixed-use commercial and retail property features prestigious retail Tenants such as Kelp Tavu and Dune Kitchen."

"A year-round coastal Mediterranean climate, a highly diverse business sector, and the vibrant, pedestrian-oriented Linden Row Walkway and Harbor Crest Arcade makes this beachside community a highly desirable commercial and retail location."

```html
<!DOCTYPE html>
<html lang="en">
<head>
<meta charset="utf-8">
<title>Bellhaven Court – Leasing Flyer</title>
<link rel="stylesheet" href="https://fonts.googleapis.com/css2?family=Michroma&family=Mulish:ital,wght@0,400;0,600;0,700;0,800;1,800&family=Parisienne&display=swap">
<style>
  :root {
    --yellow: #f6c81e;
    --navy: #1f2d7a;
    --blue: #2f6fc0;
    --ink: #2b2b2b;
    --backdrop: #e7e4df;
  }
  * { box-sizing: border-box; margin: 0; padding: 0; }
  html, body { width: 1200px; height: 830px; overflow: hidden; }
  body { background: var(--backdrop); font-family: "Mulish", sans-serif; color: var(--ink); position: relative; }

  .page { position: absolute; top: 30px; width: 546px; height: 770px; background: #fff; overflow: hidden; box-shadow: 0 2px 8px rgba(0,0,0,.15); }
  .page--front { left: 36px; }
  .page--back { left: 614px; }

  .photo { position: absolute; border-radius: 22px; overflow: hidden; }
  .photo--building { left: 20px; top: 21px; width: 506px; height: 323px; background: linear-gradient(180deg, #6aa8e8 0%, #a9cdf0 35%, #f2f2f4 55%, #d8d8dc 80%, #6b6f7a 100%); }
  .title-band { position: absolute; left: 0; top: 0; }
  .property-title { position: absolute; left: 36px; top: 38px; font-family: "Michroma", sans-serif; font-size: 23px; color: #111; letter-spacing: .5px; }

  .headline { position: absolute; left: 0; width: 546px; top: 358px; text-align: center; font-size: 14.5px; font-weight: 700; color: var(--navy); }
  .subhead { position: absolute; z-index: 2; left: 114px; top: 386px; width: 290px; font-size: 13.5px; font-weight: 800; font-style: italic; color: var(--blue); line-height: 1.3; letter-spacing: -.2px; white-space: nowrap; }
  .floor-plan { position: absolute; left: 23px; top: 420px; width: 162px; height: 174px; background: linear-gradient(135deg, #f4f4f6, #e2e2ea); border: 1px solid #c9c9d2; }
  .description { position: absolute; left: 212px; top: 446px; width: 166px; font-size: 7px; line-height: 1.28; text-align: justify; color: #333; }
  .description p + p { margin-top: 8px; }
  .photo--balcony { left: 411px; top: 390px; width: 135px; height: 200px; border-radius: 18px 0 0 18px; background: linear-gradient(180deg, #9cc8ee 0%, #cfe3f2 40%, #c7c3b8 65%, #5b7d3e 100%); }

  .bottom-art { position: absolute; left: 0; top: 0; }
  .script { position: absolute; font-family: "Parisienne", cursive; color: rgba(150,150,150,.55); font-size: 30px; white-space: nowrap; }
  .contact { position: absolute; font-size: 10px; color: #333; line-height: 1.45; white-space: nowrap; }
  .contact .name { font-size: 14px; font-weight: 800; color: var(--navy); }
  .contact svg { width: 9px; height: 9px; vertical-align: -1px; margin-right: 2px; }
  .brand { position: absolute; width: 124px; text-align: center; }
  .brand .mark { width: 46px; height: 46px; border-radius: 50%; background: var(--yellow); margin: 0 auto 12px; }
  .brand .name { font-size: 13px; font-weight: 700; letter-spacing: 3px; color: #222; line-height: 1.3; }
  .main-phone { position: absolute; top: 733px; font-size: 15px; font-weight: 800; color: #222; white-space: nowrap; }
  .main-phone svg { width: 13px; height: 13px; vertical-align: -1px; margin-right: 2px; }
  .footer-line { position: absolute; top: 757px; font-size: 9px; color: #333; white-space: nowrap; }
  .footer-line svg { width: 8px; height: 8px; vertical-align: -1px; margin-right: 2px; }

  .photo--reception { left: 20px; top: 22px; width: 248px; height: 169px; background: linear-gradient(180deg, #e9e6da 0%, #d9d2bf 50%, #b58a52 80%, #9a9386 100%); }
  .photo--lobby { left: 277px; top: 22px; width: 249px; height: 169px; background: linear-gradient(90deg, #c9c4bb 0%, #5e5e62 40%, #4f4f53 70%, #a39a90 100%); }
  .photo--office { left: 277px; top: 205px; width: 249px; height: 169px; background: linear-gradient(180deg, #d9cfb6 0%, #e8e0c8 45%, #9db8c9 55%, #b6ab92 75%, #8a8373 100%); }
  .divider-dot { position: absolute; left: 258px; top: 184px; width: 28px; height: 28px; border-radius: 50%; background: var(--yellow); border: 3px solid #fff; z-index: 2; }
  .amenities { position: absolute; left: 20px; top: 205px; width: 248px; height: 169px; border-radius: 18px; background: linear-gradient(180deg, #eeeeee, #d6d6d6); padding: 10px 8px 0 12px; }
  .amenities h2 { font-size: 14px; font-weight: 700; letter-spacing: 3px; color: var(--blue); margin-left: 8px; }
  .amenities ul { list-style: none; margin-top: 3px; }
  .amenities li { position: relative; padding-left: 13px; font-size: 6.8px; line-height: 1.3; color: #333; margin-bottom: 7px; text-align: justify; }
  .amenities li svg { position: absolute; left: 0; top: 0; width: 9px; height: 9px; }
  .map { position: absolute; left: 41px; top: 389px; width: 464px; height: 202px; border-radius: 18px; background: linear-gradient(135deg, #f6f0c9 0%, #efe6b3 50%, #f3ebc2 100%); box-shadow: 0 2px 6px rgba(0,0,0,.2); }
</style>
</head>
<body>

<section class="page page--front">
  <div class="photo photo--building" role="img" aria-label="Photo of the three-story white Bellhaven Court building on Ocean Ave with palm trees and blue sky"></div>
  <svg class="title-band" width="546" height="110" viewBox="0 0 546 110">
    <path d="M0 0 H424 C400 40 380 70 330 78 C240 88 120 82 20 84 H0 Z" fill="var(--yellow)"/>
  </svg>
  <h1 class="property-title">BELLHAVEN COURT</h1>

  <p class="headline">Rare Class A Oceanfront Office Space in the heart of Santa Monica</p>
  <p class="subhead">2nd Floor Office Space consisting of<br>16,159 square feet with private balconies.</p>

  <div class="floor-plan" role="img" aria-label="2nd floor space plan of Bellhaven Court with suites outlined"></div>
  <div class="description">
    <p>Bellhaven Court is one of Santa Monica's rare commercial properties that is both strategically located in the city's burgeoning central business district, yet ideally positioned on palm-lined Ocean Ave directly across from the Pacific Ocean. Built in 1987, the 3-story mixed-use commercial and retail property features prestigious retail Tenants such as Kelp Tavu and Dune Kitchen.</p>
    <p>A year-round coastal Mediterranean climate, a highly diverse business sector, and the vibrant, pedestrian-oriented Linden Row Walkway and Harbor Crest Arcade makes this beachside community a highly desirable commercial and retail location.</p>
  </div>
  <div class="photo photo--balcony" role="img" aria-label="Photo of a private balcony with planters overlooking palm trees and the ocean"></div>

  <svg class="bottom-art" width="546" height="770" viewBox="0 0 546 770">
    <defs>
      <linearGradient id="greyFront" x1="0" y1="0" x2="0" y2="1">
        <stop offset="0" stop-color="#e2e2e2"/><stop offset="1" stop-color="#f7f7f7"/>
      </linearGradient>
    </defs>
    <path d="M0 600 C150 610 330 625 546 632 V770 H0 Z" fill="url(#greyFront)"/>
    <path d="M0 700 C160 690 330 700 430 710 C490 716 530 700 546 690 V770 H0 Z" fill="var(--yellow)"/>
    <path d="M300 700 C360 660 400 640 380 610 C420 640 440 690 430 710 Z" fill="#fff" opacity=".6"/>
  </svg>
  <div class="script" style="left:150px; top:604px; transform:rotate(6deg);">Prestigious Workplace</div>

  <div class="contact" style="left:46px; top:626px; transform:rotate(5deg);">
    <div class="name">Trevor L. Ashdown</div>
    <div><svg viewBox="0 0 10 10"><circle cx="5" cy="5" r="4.5" fill="none" stroke="#333"/><path d="M3 2.5l1 1-.6.8c.4.8 1 1.4 1.8 1.8l.8-.6 1 1-.7.9C4.8 7.2 2.8 5.2 2.6 3.2Z" fill="#333"/></svg>(310) 555-0142</div>
    <div><svg viewBox="0 0 10 10"><rect x="1" y="2.5" width="8" height="5" fill="none" stroke="#333"/><path d="M1 2.5l4 3 4-3" fill="none" stroke="#333"/></svg>trev@verlindeproperty.com</div>
  </div>
  <div class="contact" style="left:222px; top:654px; transform:rotate(5deg);">
    <div class="name">Mark Oda</div>
    <div><svg viewBox="0 0 10 10"><circle cx="5" cy="5" r="4.5" fill="none" stroke="#333"/><path d="M3 2.5l1 1-.6.8c.4.8 1 1.4 1.8 1.8l.8-.6 1 1-.7.9C4.8 7.2 2.8 5.2 2.6 3.2Z" fill="#333"/></svg>(310) 555-0187</div>
    <div><svg viewBox="0 0 10 10"><rect x="1" y="2.5" width="8" height="5" fill="none" stroke="#333"/><path d="M1 2.5l4 3 4-3" fill="none" stroke="#333"/></svg>mark@verlindeproperty.com</div>
  </div>

  <div class="brand" style="left:405px; top:622px;">
    <div class="mark"></div>
    <div class="name">VERLINDE<br>PROPERTY</div>
  </div>

  <div class="main-phone" style="left:108px;"><svg viewBox="0 0 10 10"><circle cx="5" cy="5" r="4.5" fill="none" stroke="#222"/><path d="M3 2.5l1 1-.6.8c.4.8 1 1.4 1.8 1.8l.8-.6 1 1-.7.9C4.8 7.2 2.8 5.2 2.6 3.2Z" fill="#222"/></svg>(310) 555-0142</div>
  <div class="footer-line" style="left:90px;"><svg viewBox="0 0 10 10"><path d="M5 9.5C2 6 1.5 4.8 1.5 3.8a3.5 3.5 0 0 1 7 0c0 1-.5 2.2-3.5 5.7Z" fill="#333"/><circle cx="5" cy="3.8" r="1.2" fill="#fff"/></svg>5127 N Harlow Ave, Suite 210 West Hollywood, Ca. 90069</div>
  <div class="footer-line" style="left:368px;"><svg viewBox="0 0 10 10"><circle cx="5" cy="5" r="4.3" fill="none" stroke="#333"/><path d="M.7 5h8.6M5 .7c-2.4 2.6-2.4 6 0 8.6M5 .7c2.4 2.6 2.4 6 0 8.6" fill="none" stroke="#333" stroke-width=".7"/></svg>www.verlindeproperty.com</div>
</section>

<section class="page page--back">
  <div class="photo photo--reception" role="img" aria-label="Photo of the office reception area with a curved wood front desk"></div>
  <div class="photo photo--lobby" role="img" aria-label="Photo of the elevator lobby with dark panels and red carpet mats"></div>
  <div class="divider-dot"></div>

  <div class="amenities">
    <h2>BUILDING AMENITIES:</h2>
    <ul>
      <li><svg viewBox="0 0 10 10"><rect x=".5" y="1.5" width="7" height="7" fill="none" stroke="#333"/><path d="M2 5l2 2 5-6" fill="none" stroke="#333" stroke-width="1.4"/></svg>Prestigious, oceanfront location with unobstructed ocean views</li>
      <li><svg viewBox="0 0 10 10"><rect x=".5" y="1.5" width="7" height="7" fill="none" stroke="#333"/><path d="M2 5l2 2 5-6" fill="none" stroke="#333" stroke-width="1.4"/></svg>Situated in the heart of Santa Monica's downtown business district</li>
      <li><svg viewBox="0 0 10 10"><rect x=".5" y="1.5" width="7" height="7" fill="none" stroke="#333"/><path d="M2 5l2 2 5-6" fill="none" stroke="#333" stroke-width="1.4"/></svg>Walking distance to prestigious restaurants, first-class hotels and the Linden Row Walkway</li>
      <li><svg viewBox="0 0 10 10"><rect x=".5" y="1.5" width="7" height="7" fill="none" stroke="#333"/><path d="M2 5l2 2 5-6" fill="none" stroke="#333" stroke-width="1.4"/></svg>On-site parking conveniently accessible by major freeways, bus lines, and airports</li>
      <li><svg viewBox="0 0 10 10"><rect x=".5" y="1.5" width="7" height="7" fill="none" stroke="#333"/><path d="M2 5l2 2 5-6" fill="none" stroke="#333" stroke-width="1.4"/></svg>On-site management ensuring quick response to tenant's requests</li>
      <li><svg viewBox="0 0 10 10"><rect x=".5" y="1.5" width="7" height="7" fill="none" stroke="#333"/><path d="M2 5l2 2 5-6" fill="none" stroke="#333" stroke-width="1.4"/></svg>Secured building with video surveillance and tenant access key cards</li>
    </ul>
  </div>
  <div class="photo photo--office" role="img" aria-label="Photo of an empty carpeted office with windows looking out to palm trees"></div>

  <div class="map" role="img" aria-label="Street map of downtown Santa Monica marking Bellhaven Court on Ocean Ave near the beach and freeway"></div>

  <svg class="bottom-art" width="546" height="770" viewBox="0 0 546 770">
    <defs>
      <linearGradient id="greyBack" x1="0" y1="0" x2="0" y2="1">
        <stop offset="0" stop-color="#e2e2e2"/><stop offset="1" stop-color="#f7f7f7"/>
      </linearGradient>
    </defs>
    <path d="M0 632 C200 625 380 612 546 600 V770 H0 Z" fill="url(#greyBack)"/>
    <path d="M0 690 C20 705 60 716 116 710 C220 700 390 690 546 700 V770 H0 Z" fill="var(--yellow)"/>
    <path d="M116 710 C100 690 120 640 160 612 C140 650 150 690 246 700 Z" fill="#fff" opacity=".6"/>
  </svg>
  <div class="script" style="left:172px; top:606px; transform:rotate(-5deg);">Bellhaven Court</div>

  <div class="brand" style="left:24px; top:622px;">
    <div class="mark"></div>
    <div class="name">VERLINDE<br>PROPERTY</div>
  </div>

  <div class="contact" style="left:170px; top:656px; transform:rotate(-5deg);">
    <div class="name">Trevor L. Ashdown</div>
    <div><svg viewBox="0 0 10 10"><circle cx="5" cy="5" r="4.5" fill="none" stroke="#333"/><path d="M3 2.5l1 1-.6.8c.4.8 1 1.4 1.8 1.8l.8-.6 1 1-.7.9C4.8 7.2 2.8 5.2 2.6 3.2Z" fill="#333"/></svg>(310) 555-0142</div>
    <div><svg viewBox="0 0 10 10"><rect x="1" y="2.5" width="8" height="5" fill="none" stroke="#333"/><path d="M1 2.5l4 3 4-3" fill="none" stroke="#333"/></svg>trev@verlindeproperty.com</div>
  </div>
  <div class="contact" style="left:352px; top:640px; transform:rotate(-5deg);">
    <div class="name">Mark Oda</div>
    <div><svg viewBox="0 0 10 10"><circle cx="5" cy="5" r="4.5" fill="none" stroke="#333"/><path d="M3 2.5l1 1-.6.8c.4.8 1 1.4 1.8 1.8l.8-.6 1 1-.7.9C4.8 7.2 2.8 5.2 2.6 3.2Z" fill="#333"/></svg>(310) 555-0187</div>
    <div><svg viewBox="0 0 10 10"><rect x="1" y="2.5" width="8" height="5" fill="none" stroke="#333"/><path d="M1 2.5l4 3 4-3" fill="none" stroke="#333"/></svg>mark@verlindeproperty.com</div>
  </div>

  <div class="main-phone" style="left:339px;"><svg viewBox="0 0 10 10"><circle cx="5" cy="5" r="4.5" fill="none" stroke="#222"/><path d="M3 2.5l1 1-.6.8c.4.8 1 1.4 1.8 1.8l.8-.6 1 1-.7.9C4.8 7.2 2.8 5.2 2.6 3.2Z" fill="#222"/></svg>(310) 555-0142</div>
  <div class="footer-line" style="left:28px;"><svg viewBox="0 0 10 10"><circle cx="5" cy="5" r="4.3" fill="none" stroke="#333"/><path d="M.7 5h8.6M5 .7c-2.4 2.6-2.4 6 0 8.6M5 .7c2.4 2.6 2.4 6 0 8.6" fill="none" stroke="#333" stroke-width=".7"/></svg>www.verlindeproperty.com</div>
  <div class="footer-line" style="left:220px;"><svg viewBox="0 0 10 10"><path d="M5 9.5C2 6 1.5 4.8 1.5 3.8a3.5 3.5 0 0 1 7 0c0 1-.5 2.2-3.5 5.7Z" fill="#333"/><circle cx="5" cy="3.8" r="1.2" fill="#fff"/></svg>5127 N Harlow Ave, Suite 210 West Hollywood, Ca. 90069</div>
</section>

</body>
</html>
```